Data as a Product

I have a consulting firm that specializes in maximizing the value of corporate data for secondary use i.e. the provisioning of data for reporting, analysis and information to make better decisions. I have trade marked a phrase, "data as a product". The concept in a graphic that I am trying to get across is:

The manufacturing of Data
The Warehousing of Data
The Distribution of Data
The Customer use of Data
The Support of Data

Basically a graphic that shows a manufacturing workflow but the product is data. My idea is to show: (I'll try to describe in steps)

1. The manufacturing of bits and bytes by a machine
2. The assembling of those bits and bytes into components i.e. letters, words, symbols, information components
3. The warehousing of the components until needed
4. The assembling of the components into a Product.
4b. The ordering of the components via a catalogue to form a product by a consumer of information
5. The distribution and/or publishing of the product to the needed formats i.e. PDF, Word, Powerpoint, Excel, Reports, etc. for use by a consumer of the information or data product
6. The support of the customer use

I want to keep it high level, simple, basically resemble a production line of a manufactured product through its life cycle but now we're talking about data being the product.

Thank you,
Mark Torvend
mark@9rvsolutions.example
482 917 3056

Target Market(s)

Corporate enterprise, Global 1000 companies. Pretty much all functions within the corporation.

Industry/Entity Type

Trade

Requirements
Must have
• this design is going on my website at 9rvsolutions.example but it would be good to be able to print for a leave behind if that is what you are asking.

```html
<!DOCTYPE html>
<html lang="en">
<head>
<meta charset="utf-8">
<title>Data as a Product – Production Line of Data</title>
<link rel="stylesheet" href="https://fonts.googleapis.com/css2?family=Arimo:wght@700&family=Cousine:wght@700&display=swap">
<style>
  :root {
    --bg-top: #2b4862;
    --bg-mid: #6f90ad;
    --bg-low: #6487a6;
    --bg-bottom: #52769a;
    --text: #ffffff;
    --arrow: rgba(150, 170, 190, 0.75);
    --tile: #f4f6f8;
    --tile-shadow: rgba(20, 40, 60, 0.35);
    --red: #c8322a;
    --blue: #2e63b8;
    --green: #2f9447;
    --orange: #e0652a;
    --puzzle-red: #a3283a;
    --puzzle-yellow: #f2d21c;
    --puzzle-green: #6aa536;
    --puzzle-blue: #8cc0ec;
    --support-top: #2aa3e6;
    --support-bottom: #0b6fb8;
    --support-ink: #0d2f66;
  }
  html, body {
    margin: 0;
    padding: 0;
    width: 1200px;
    height: 2208px;
    overflow: hidden;
  }
  body {
    background: linear-gradient(180deg, var(--bg-top) 0%, var(--bg-mid) 45%, var(--bg-low) 75%, var(--bg-bottom) 100%);
    font-family: "Arimo", Arial, sans-serif;
    color: var(--text);
    position: relative;
  }
  .stage { position: absolute; }
  .circuit-art {
    left: 0; top: 0; width: 1200px; height: 160px;
    background:
      radial-gradient(ellipse 60% 90% at 50% 0%, rgba(235,242,248,0.55), rgba(235,242,248,0) 70%),
      linear-gradient(180deg, rgba(220,232,242,0.35), rgba(220,232,242,0));
  }
  .flow-arrow { left: 577px; width: 46px; height: 46px; }
  .binary-stream {
    left: 0; top: 228px; width: 1200px;
    font-family: "Cousine", "Courier New", monospace;
    font-weight: 700;
    font-size: 36px;
    line-height: 36px;
    text-align: center;
    white-space: pre;
  }
  .component-words {
    left: 20px; top: 522px; width: 1160px;
    text-align: center;
    font-weight: 700;
  }
  .component-words p { margin: 0; white-space: nowrap; }
  .component-words .w-lg { font-size: 33px; line-height: 39px; }
  .component-words .w-md { font-size: 27px; line-height: 32px; }
  .component-words .w-sm { font-size: 22px; line-height: 28px; }
  .warehouse {
    top: 812px; width: 486px; height: 240px;
    background: linear-gradient(160deg, #e9edf1 0%, #a9c7dc 45%, #8fbf5a 75%, #dfe4e8 100%);
    clip-path: polygon(50% 0, 100% 40%, 100% 78%, 50% 100%, 0 78%, 0 40%);
  }
  .warehouse.left { left: 87px; }
  .warehouse.right { left: 633px; }
  .assembly-puzzle {
    left: 425px; top: 1140px; width: 400px; height: 345px;
    border-radius: 40px;
    background: conic-gradient(from 0deg at 50% 50%,
      var(--puzzle-yellow) 0deg, var(--puzzle-yellow) 70deg,
      var(--puzzle-green) 110deg, var(--puzzle-green) 160deg,
      var(--puzzle-blue) 200deg, var(--puzzle-blue) 250deg,
      var(--puzzle-red) 290deg, var(--puzzle-red) 340deg,
      var(--puzzle-yellow) 360deg);
    filter: blur(6px);
    opacity: 0.92;
  }
  .formats {
    left: 99px; top: 1606px; width: 1001px; height: 160px;
    display: flex; justify-content: space-between;
  }
  .format-tile {
    width: 155px; height: 155px;
    background: var(--tile);
    border-radius: 14px;
    box-shadow: 6px 8px 10px var(--tile-shadow);
    display: flex; align-items: center; justify-content: center;
  }
  .format-mark { width: 84px; height: 96px; border-radius: 8px; }
  .format-mark.pdf { background: var(--red); }
  .format-mark.doc { background: var(--blue); }
  .format-mark.sheet { background: var(--green); }
  .format-mark.slides { background: var(--orange); }
  .support-badge {
    left: 425px; top: 1882px; width: 335px; height: 288px;
  }
  .support-plate {
    position: absolute; left: 0; top: 0; width: 335px; height: 175px;
    background: linear-gradient(180deg, var(--support-top), var(--support-bottom));
    border-radius: 22px 22px 10px 10px;
    box-shadow: 0 6px 12px var(--tile-shadow);
    display: flex; align-items: center; justify-content: center;
  }
  .support-plate span {
    font-size: 50px; letter-spacing: 1px; color: var(--support-ink);
  }
  .support-base {
    position: absolute; left: 10px; top: 150px; width: 315px; height: 138px;
    background: linear-gradient(180deg, #e7edf2, #c2ccd6);
    border-radius: 0 0 12px 12px;
  }
  .support-chat {
    position: absolute; left: 88px; top: 155px; width: 160px; height: 120px;
    border-radius: 50%;
    background: radial-gradient(circle at 50% 40%, #ffd54a, #f08a12);
  }
</style>
</head>
<body>
  <div class="stage circuit-art" role="img" aria-label="Circuit board traces running down from the top edge"></div>

  <svg class="stage flow-arrow" style="top:168px" viewBox="0 0 46 46"><path d="M16 2h14v20h12L23 44 4 22h12z" fill="var(--arrow)"/></svg>

  <div class="stage binary-stream">0101100110110101010101010101110010101011010110010
1010100110110010101011010110001011111101001011101
1110101111000101010100001001101001011110010101010
0010000110010101011001000010010011001100100011011
1010001010101101011010010010101001010101101001100</div>

  <svg class="stage flow-arrow" style="top:444px" viewBox="0 0 46 46"><path d="M16 2h14v20h12L23 44 4 22h12z" fill="var(--arrow)"/></svg>

  <div class="stage component-words">
    <p class="w-lg">data number letter &amp; information 14 sample words 5% title consulting</p>
    <p class="w-lg">text software global integration 1 space drive 1541 analysis business</p>
    <p class="w-lg">reseller ranging work #&nbsp; 12 structured sample words&nbsp; title component</p>
    <p class="w-md">internet number @ * letter unstructured 1 sample data 14 * title application letter 25</p>
    <p class="w-sm">goals perspective &amp; information 51 sample words 15% title component text number letter&nbsp; information</p>
  </div>

  <svg class="stage flow-arrow" style="top:760px" viewBox="0 0 46 46"><path d="M16 2h14v20h12L23 44 4 22h12z" fill="var(--arrow)"/></svg>

  <div class="stage warehouse left" role="img" aria-label="Isometric data warehouse with rows of server racks"></div>
  <div class="stage warehouse right" role="img" aria-label="Second isometric data warehouse with rows of server racks"></div>

  <svg class="stage flow-arrow" style="top:1072px" viewBox="0 0 46 46"><path d="M16 2h14v20h12L23 44 4 22h12z" fill="var(--arrow)"/></svg>

  <div class="stage assembly-puzzle" role="img" aria-label="Four interlocking puzzle pieces in red, yellow, blue and green forming the product"></div>

  <svg class="stage flow-arrow" style="top:1520px" viewBox="0 0 46 46"><path d="M16 2h14v20h12L23 44 4 22h12z" fill="var(--arrow)"/></svg>

  <div class="stage formats">
    <div class="format-tile"><div class="format-mark pdf"></div></div>
    <div class="format-tile"><div class="format-mark doc"></div></div>
    <div class="format-tile"><div class="format-mark sheet"></div></div>
    <div class="format-tile"><div class="format-mark slides"></div></div>
    <div class="format-tile">
      <svg width="120" height="110" viewBox="0 0 120 110" aria-label="Report chart">
        <rect x="4" y="4" width="112" height="102" fill="#fff" stroke="#b8c2cc" stroke-width="2"/>
        <path d="M10 100 L10 70 L30 55 L50 62 L70 40 L90 50 L110 30 L110 100 Z" fill="#f2a21c"/>
        <path d="M10 100 L10 82 L30 72 L50 78 L70 62 L90 70 L110 55 L110 100 Z" fill="#d7472c"/>
        <path d="M10 100 L10 92 L30 86 L50 90 L70 80 L90 84 L110 76 L110 100 Z" fill="#3f8fcf"/>
      </svg>
    </div>
  </div>

  <svg class="stage flow-arrow" style="top:1812px" viewBox="0 0 46 46"><path d="M16 2h14v20h12L23 44 4 22h12z" fill="var(--arrow)"/></svg>

  <div class="stage support-badge">
    <div class="support-base"></div>
    <div class="support-plate"><span>SUPPORT</span></div>
    <div class="support-chat" role="img" aria-label="Round orange badge with chat speech bubbles"></div>
  </div>
</body>
</html>
```